Need business card designed for a Mobile RV Repair business

I need a business card designed

Welding sparks

Industry/Entity Type

Rv Repair , Mobile Welding & Fabrication

Contact Information for Business Card

****

Colors
0054AA
0677BA
7BADD7
CADEEF
E8F1F8

Requirements
Nice to have
• welding sparks, list of services, welding vector

```html
<!DOCTYPE html>
<html lang="en">
<head>
<meta charset="UTF-8">
<title>Roadside Rig Works — Business Card</title>
<link rel="stylesheet" href="https://fonts.googleapis.com/css2?family=Montserrat:wght@400;500;700&display=swap">
<style>
  :root {
    --bg: #2e2e2e;
    --card: #ffffff;
    --card-shade: #ececec;
    --teal: #12867b;
    --teal-deep: #0d7469;
    --orange: #ef8a17;
    --yellow: #f3d80c;
    --ink: #3a3a3a;
    --ink-soft: #555555;
    --white: #ffffff;
    --faint: #eef1f0;
  }
  * { box-sizing: border-box; margin: 0; padding: 0; }
  html, body { width: 1200px; height: 900px; overflow: hidden; }
  body {
    background: var(--bg);
    font-family: "Montserrat", sans-serif;
    position: relative;
  }
  .card {
    position: absolute;
    left: 250px;
    width: 700px;
    height: 400px;
    background: linear-gradient(160deg, var(--card) 40%, var(--card-shade) 100%);
    overflow: hidden;
  }
  .card--services { top: 40px; }
  .card--contact { top: 470px; }

  .brand {
    position: absolute;
    display: flex;
    align-items: center;
    gap: 12px;
  }
  .brand__dot {
    width: 22px; height: 22px;
    border-radius: 50%;
    background: var(--teal);
    flex: none;
  }
  .brand__name {
    font-weight: 700;
    font-size: 20px;
    line-height: 1;
    color: var(--ink);
    white-space: nowrap;
  }
  .card--services .brand { left: 40px; top: 186px; }
  .card--contact .brand { left: 40px; top: 90px; }

  .services {
    position: absolute;
    right: 40px;
    top: 48px;
    text-align: right;
  }
  .services__title {
    font-weight: 700;
    font-size: 24px;
    color: var(--teal);
    margin-bottom: 10px;
  }
  .services__list { list-style: none; }
  .services__item {
    font-size: 16px;
    color: var(--ink-soft);
    line-height: 30px;
    display: flex;
    justify-content: flex-end;
    align-items: center;
    gap: 10px;
  }
  .services__item svg { width: 14px; height: 14px; flex: none; }

  .faint-art {
    position: absolute;
    right: 60px;
    top: 40px;
    width: 300px;
    height: 210px;
    background: radial-gradient(ellipse at center, var(--faint) 0%, rgba(238,241,240,0) 70%);
  }
  .wave { position: absolute; inset: 0; width: 700px; height: 400px; }

  .contact {
    position: absolute;
    left: 150px;
    bottom: 38px;
    color: var(--white);
  }
  .contact__name {
    font-size: 22px;
    font-weight: 500;
    margin-bottom: 10px;
  }
  .contact__name strong { color: var(--yellow); font-weight: 700; text-transform: uppercase; }
  .contact__line {
    font-size: 16px;
    display: flex;
    align-items: center;
    gap: 8px;
  }
  .contact__line svg { width: 16px; height: 16px; }
  .contact__sep { margin: 0 4px; }
</style>
</head>
<body>

<section class="card card--services">
  <div class="brand">
    <span class="brand__dot"></span>
    <span class="brand__name">Roadside Rig Works</span>
  </div>

  <div class="services">
    <h2 class="services__title">Our Services</h2>
    <ul class="services__list">
      <li class="services__item">RV Repair <svg viewBox="0 0 14 14"><path d="M1 12 L13 7 L1 2 L5 7 Z" fill="#12867b"/></svg></li>
      <li class="services__item">Electrical <svg viewBox="0 0 14 14"><path d="M1 12 L13 7 L1 2 L5 7 Z" fill="#12867b"/></svg></li>
      <li class="services__item">Plumbing <svg viewBox="0 0 14 14"><path d="M1 12 L13 7 L1 2 L5 7 Z" fill="#12867b"/></svg></li>
      <li class="services__item">Mobile Welding <svg viewBox="0 0 14 14"><path d="M1 12 L13 7 L1 2 L5 7 Z" fill="#12867b"/></svg></li>
      <li class="services__item">General repairs &amp; modifications <svg viewBox="0 0 14 14"><path d="M1 12 L13 7 L1 2 L5 7 Z" fill="#12867b"/></svg></li>
      <li class="services__item">Custom fabrication <svg viewBox="0 0 14 14"><path d="M1 12 L13 7 L1 2 L5 7 Z" fill="#12867b"/></svg></li>
      <li class="services__item">Gates/Fences <svg viewBox="0 0 14 14"><path d="M1 12 L13 7 L1 2 L5 7 Z" fill="#12867b"/></svg></li>
      <li class="services__item">Aluminum welding <svg viewBox="0 0 14 14"><path d="M1 12 L13 7 L1 2 L5 7 Z" fill="#12867b"/></svg></li>
    </ul>
  </div>
</section>

<section class="card card--contact">
  <div class="faint-art" role="img" aria-label="Faint background illustration of a welder at work with sparks"></div>

  <svg class="wave" viewBox="0 0 700 400" aria-hidden="true">
    <defs>
      <linearGradient id="edge" x1="0" y1="0" x2="1" y2="0">
        <stop offset="0" stop-color="#ef8a17"/>
        <stop offset="0.55" stop-color="#f3d80c"/>
        <stop offset="1" stop-color="#ef8a17"/>
      </linearGradient>
      <linearGradient id="band" x1="0" y1="0" x2="1" y2="1">
        <stop offset="0" stop-color="#14907f"/>
        <stop offset="1" stop-color="#0d7469"/>
      </linearGradient>
    </defs>
    <path d="M0,400 L0,330 C110,220 260,270 430,250 C570,232 650,190 700,150 L700,400 Z" fill="url(#band)"/>
    <path d="M0,330 C110,220 260,270 430,250 C570,232 650,190 700,150" fill="none" stroke="url(#edge)" stroke-width="6"/>
  </svg>

  <div class="brand">
    <span class="brand__dot"></span>
    <span class="brand__name">Roadside Rig Works</span>
  </div>

  <div class="contact">
    <p class="contact__name"><strong>Marco Delgado</strong> | Owner</p>
    <p class="contact__line">
      <svg viewBox="0 0 16 16"><path d="M3 2 L6 2 L7 5 L5 6.5 C6 8.5 7.5 10 9.5 11 L11 9 L14 10 L14 13 C8 13.5 2.5 8 3 2 Z" fill="#f3d80c"/></svg>
      555.201.4477
      <span class="contact__sep">|</span>
      <svg viewBox="0 0 16 16"><rect x="1.5" y="3.5" width="13" height="9" rx="1" fill="#f3d80c"/><path d="M2 4 L8 9 L14 4" fill="none" stroke="#0d7469" stroke-width="1.3"/></svg>
      roadsiderig@example.com
    </p>
  </div>
</section>

</body>
</html>
```